Plumbing business card and logo desgin

Need a new business card and logo for a plumbing business based in Warragul, Australia. Business name is 9Brook plumbing & air-conditioning. We service all plumbing and gasfitting needs and installation of air-conditioning. We clear blocked drains, install new hot water systems, central heating, new and existing homes, roofing, sanitary and drainage.
i would like to have a space on there for website, email, phone, licence number and what we do as a company.
i would like a water droplet to be incorporated into the design to try and stand out that we are a plumbing business

Contact Information for Business Card

phone number: 0497215836
Licence Number: 873614

Logo Text

9Brook Plumbing & Air-Conditioning

```html
<!DOCTYPE html>
<html lang="en">
<head>
<meta charset="utf-8">
<title>9Brook Plumbing &amp; Air-Conditioning – Business Card</title>
<link rel="stylesheet" href="https://fonts.googleapis.com/css2?family=Barlow+Condensed:wght@400;500&family=Montserrat:wght@600;800&display=swap">
<style>
  :root {
    --page: #e6e8eb;
    --card: #f4f5f6;
    --brand-blue: #3a5ba8;
    --drop-blue: #4a9bd6;
    --ink: #4a4a4a;
    --rule: #555555;
    --band: #5e5e5e;
  }
  html, body {
    margin: 0;
    width: 1200px;
    height: 936px;
    overflow: hidden;
    background: var(--page);
  }
  .card {
    position: absolute;
    left: 40px;
    top: 123px;
    width: 1120px;
    height: 690px;
    background: var(--card);
    box-shadow: 0 10px 30px rgba(0,0,0,0.15);
    overflow: hidden;
  }
  .card-texture {
    position: absolute;
    inset: 0;
    background: radial-gradient(ellipse at 60% 30%, #fbfbfc 0%, #eef0f2 70%, #e8eaec 100%);
  }
  .logo-name {
    position: absolute;
    left: 0;
    right: 0;
    top: 95px;
    text-align: center;
    font-family: "Montserrat", sans-serif;
    font-weight: 800;
    color: var(--brand-blue);
    font-size: 50px;
    line-height: 1.25;
    letter-spacing: 1px;
  }
  .logo-name .mark {
    display: inline-block;
    width: 22px;
    height: 22px;
    border-radius: 50%;
    background: var(--brand-blue);
    margin-right: 16px;
    vertical-align: middle;
    position: relative;
    top: -4px;
  }
  .divider {
    position: absolute;
    left: 48px;
    right: 42px;
    top: 340px;
    height: 2px;
    background: var(--rule);
  }
  .person {
    position: absolute;
    right: 650px;
    top: 450px;
    text-align: right;
  }
  .person-name {
    font-family: "Montserrat", sans-serif;
    font-weight: 800;
    color: var(--brand-blue);
    font-size: 34px;
    letter-spacing: 7px;
    margin-right: -7px;
  }
  .person-role {
    font-family: "Barlow Condensed", sans-serif;
    font-size: 30px;
    color: var(--ink);
    margin-top: 4px;
  }
  .column-rule {
    position: absolute;
    left: 563px;
    top: 432px;
    width: 3px;
    height: 118px;
    background: var(--brand-blue);
  }
  .contacts {
    position: absolute;
    left: 630px;
    top: 428px;
    margin: 0;
    padding: 0;
    list-style: none;
    font-family: "Barlow Condensed", sans-serif;
    font-size: 31px;
    color: var(--ink);
  }
  .contacts li {
    display: flex;
    align-items: center;
    height: 42px;
  }
  .contacts svg {
    width: 28px;
    height: 28px;
    margin-right: 14px;
    flex: none;
  }
  .licence-band {
    position: absolute;
    left: 0;
    right: 0;
    top: 612px;
    height: 60px;
    background: var(--band);
    text-align: center;
    font-family: "Barlow Condensed", sans-serif;
    font-size: 31px;
    line-height: 60px;
    color: var(--drop-blue);
  }
</style>
</head>
<body>
  <div class="card">
    <div class="card-texture" role="img" aria-label="Soft background of scattered water droplets"></div>

    <div class="logo-name"><span class="mark"></span>9Brook Plumbing<br>&amp; Air-Conditioning</div>

    <div class="divider"></div>

    <div class="person">
      <div class="person-name">LIAM CARROW</div>
      <div class="person-role">Owner/ CEO</div>
    </div>

    <div class="column-rule"></div>

    <ul class="contacts">
      <li>
        <svg viewBox="0 0 28 28" fill="none" stroke="#3a5ba8" stroke-width="1.8">
          <circle cx="14" cy="14" r="12"/>
          <path d="M10 8.5c-1 .6-1.4 1.6-1 2.8 1.2 3.4 3.8 6 7 7.4 1.2.5 2.3.1 3-.9l-2.4-2-1.4 1c-1.7-.9-3-2.2-3.9-3.9l1-1.4z"/>
        </svg>
        049 721 5836
      </li>
      <li>
        <svg viewBox="0 0 28 28" fill="none" stroke="#3a5ba8" stroke-width="1.8">
          <circle cx="14" cy="14" r="12"/>
          <circle cx="14" cy="14" r="4"/>
          <path d="M18 10v5.5c0 1.6 2.5 1.6 2.5 0V14a6.5 6.5 0 1 0-2.8 5.3"/>
        </svg>
        hello@ninebrookplumbing.com
      </li>
      <li>
        <svg viewBox="0 0 28 28" fill="none" stroke="#3a5ba8" stroke-width="1.6">
          <circle cx="14" cy="14" r="12"/>
          <ellipse cx="14" cy="14" rx="5.5" ry="12"/>
          <path d="M2 14h24M4 8h20M4 20h20"/>
        </svg>
        www.ninebrookplumbing.com
      </li>
    </ul>

    <div class="licence-band">Licence Number: 873614</div>
  </div>
</body>
</html>
```